Italian restaurant needs new site

Need to make our website better.

Must have reservation module

Must be able to sell wine tasting tours and wine pairing tours and intégrate with lumo desk

Blog

Social media

Wandermeter ranking and last review.

Number of Pages Required

1 page

Font styles to use
Serif

Requirements
Must have
• Reservation module
• Marketplace to buy wine pairings and gift certificates
• Wandermeter review
• Chatterbay posts
• All info from old site

```html
<!DOCTYPE html>
<html lang="en">
<head>
<meta charset="utf-8">
<title>Vellora Bistro – Italian Cuisine &amp; Wine Bar</title>
<link rel="stylesheet" href="https://fonts.googleapis.com/css2?family=Cinzel:wght@400;700&family=Cormorant+Garamond:wght@500;600&family=Open+Sans:wght@400;600;700&display=swap">
<style>
:root{
  --wine:#8a1021;
  --wine-deep:#6a0a17;
  --ink:#262626;
  --text:#5a5a5a;
  --muted:#8a8a8a;
  --paper:#ffffff;
  --mist:#f3f3f3;
  --night:#1c1c1c;
  --night-2:#262626;
  --line:#dddddd;
}
*{margin:0;padding:0;box-sizing:border-box}
html,body{width:1200px;height:4569px;overflow:hidden}
body{background:var(--paper);font-family:"Open Sans",Arial,sans-serif;color:var(--text);position:relative}
section,header,footer{position:absolute;left:0;width:1200px}
.abs{position:absolute}
.center{left:0;width:1200px;text-align:center}
.title{font-family:"Cinzel",Georgia,serif;font-weight:700;font-size:28px;letter-spacing:1px;color:var(--ink)}
.title em{font-style:normal;color:var(--wine)}
.title.light{color:#fff}
.rule{position:absolute;left:550px;width:100px;height:2px;background:var(--wine)}
.rule.light{background:#fff}
.rule::after{content:"";position:absolute;left:46px;top:-3px;width:8px;height:8px;border-radius:50%;background:inherit}
.lead{font-weight:700;font-size:13.5px;color:var(--ink)}
.body{font-size:12.5px;line-height:22px;color:var(--text)}
.light-text{color:#f2f2f2}
.btn{display:inline-block;font-family:"Open Sans",Arial,sans-serif;font-weight:700;font-size:11px;letter-spacing:.5px;text-transform:uppercase;border-radius:4px;padding:0 18px;height:32px;line-height:32px;color:#fff}
.scallop-bottom{position:absolute;left:0;bottom:0;width:1200px;height:9px;background:radial-gradient(circle at 7px 9px,var(--edge,#fff) 6px,transparent 6.6px) repeat-x;background-size:14px 9px}
.scallop-top{position:absolute;left:0;top:0;width:1200px;height:9px;background:radial-gradient(circle at 7px 0,var(--edge,#fff) 6px,transparent 6.6px) repeat-x;background-size:14px 9px}

/* top bar */
.topbar{top:0;height:43px;background:var(--wine-deep)}
.topbar .item{position:absolute;top:8px;height:27px;line-height:27px;font-size:11px;font-weight:700;color:#fff;border-radius:14px;padding:0 14px 0 32px;background:#2a0a0f}
.topbar .item svg{position:absolute;left:10px;top:6px}
.topbar .phone{background:none;left:592px}

/* header */
.site-header{top:43px;height:125px;background:#fff}
.brand{left:76px;top:40px;font-family:"Cinzel",Georgia,serif;font-weight:700;font-size:30px;color:var(--wine);letter-spacing:1px}
.brand-dot{display:inline-block;width:12px;height:12px;border-radius:50%;background:var(--wine);margin-right:10px;vertical-align:middle}
.nav{left:440px;top:84px;display:flex}
.nav a{font-family:"Cinzel",Georgia,serif;font-size:14px;color:var(--ink);text-decoration:none;padding:0 26px;border-left:1px solid var(--line);line-height:20px}
.nav a:first-child{border-left:none;color:var(--wine);font-weight:700;position:relative}
.nav a:first-child::after{content:"";position:absolute;left:26px;right:26px;bottom:-8px;height:2px;background:var(--wine)}

/* hero */
.hero{top:168px;height:526px;background:radial-gradient(ellipse at 78% 45%,#6b1420 0%,#3a1a12 22%,#1a120e 50%,#0d0b0a 80%)}
.hero-photo{position:absolute;inset:0}
.hero h1{position:absolute;left:82px;top:212px;font-family:"Cormorant Garamond",Georgia,serif;font-weight:600;font-size:34px;line-height:38px;color:#fff;letter-spacing:.5px}
.dots{position:absolute;left:82px;top:340px;display:flex;gap:6px}
.dots i{width:9px;height:9px;border-radius:50%;background:#fff;opacity:.55}
.dots i:first-child{opacity:1}

/* welcome */
.welcome{top:694px;height:372px;background:#fff}

/* reservation */
.reserve{top:1066px;height:311px;background:linear-gradient(90deg,#140f0c 0%,#2b2018 35%,#1d1612 65%,#0f0c0a 100%)}
.field{position:absolute;top:179px;width:192px;height:38px;background:#fff;border-radius:3px;font-size:11px;color:#999;line-height:38px;padding-left:12px}
.submit{position:absolute;top:179px;left:923px;width:195px;height:38px;background:var(--wine);border-radius:3px;color:#fff;font-size:11px;font-weight:700;text-align:center;line-height:38px}

/* menu */
.menu{top:1377px;height:710px;background:#fafafa}
.dish{position:absolute;width:329px;height:221px;border:5px solid #2b2b2b;box-shadow:0 2px 6px rgba(0,0,0,.25)}
.dish .label{position:absolute;left:0;right:0;bottom:0;height:40px;background:rgba(20,20,20,.65);font-family:"Cinzel",Georgia,serif;font-weight:700;font-size:20px;color:#fff;text-align:center;line-height:40px;letter-spacing:1px}

/* atmosphere */
.atmos{top:2087px;height:350px;background:var(--wine)}
.btn.outline{border:1px solid #fff;background:#2a0a0f}

/* blog */
.blog{top:2437px;height:588px;background:var(--mist)}
.post{position:absolute;top:189px;width:329px}
.post .pic{height:176px;position:relative}
.post .date{position:absolute;left:0;top:0;width:62px;height:86px;background:var(--wine);color:#fff;text-align:center;font-weight:700}
.post .date b{display:block;font-size:22px;padding-top:8px}
.post .date span{display:block;font-size:10px}
.post h3{font-family:"Cinzel",Georgia,serif;font-weight:700;font-size:15px;color:var(--ink);margin-top:22px}
.post p{font-size:11px;line-height:16px;color:var(--text);margin-top:10px;width:300px}
.post .meta{margin-top:14px;padding-top:10px;border-top:1px solid var(--line);font-size:10px;color:var(--muted)}
.post .meta b{color:var(--ink)}

/* customers */
.customers{top:3025px;height:530px;background:linear-gradient(90deg,#1b1310 0%,#3a2a22 30%,#2a1e18 60%,#120d0b 100%)}
.avatar{position:absolute;top:161px;width:104px;height:104px;border-radius:50%;border:4px solid #fff;background:linear-gradient(160deg,#8d7466,#4a3a33)}
.cname{position:absolute;top:292px;width:200px;text-align:center;font-family:"Cinzel",Georgia,serif;font-weight:700;font-size:14px;color:#fff}
.arrow{position:absolute;top:190px}
.quote{position:absolute;left:82px;top:344px;width:1036px;height:134px;background:rgba(255,255,255,.13);padding:22px 110px 0;text-align:center;font-size:12.5px;line-height:22px;color:#fff}
.quote .mark{position:absolute;left:30px;top:6px;font-family:Georgia,serif;font-size:70px;color:rgba(255,255,255,.45);line-height:70px}

/* wine tours */
.tours{top:3555px;height:633px;background:#fff}
.tours .band{position:absolute;left:0;top:0;width:1200px;height:176px;background:var(--wine)}
.tour{position:absolute;top:185px;width:503px}
.tour .pic{height:256px}
.tour h3{font-family:"Cinzel",Georgia,serif;font-weight:700;font-size:27px;color:var(--ink);text-align:center;margin-top:22px;letter-spacing:1px}
.tour p{font-size:12px;line-height:21px;text-align:center;color:var(--text);margin-top:8px}

/* footer */
.site-footer{top:4188px;height:326px;background:linear-gradient(180deg,#222 0%,#1a1a1a 100%)}
.site-footer h4{position:absolute;top:44px;font-family:"Cinzel",Georgia,serif;font-weight:400;font-size:17px;color:#fff;letter-spacing:1px}
.links{position:absolute;left:82px;top:96px;list-style:none}
.links li{font-size:12px;color:#ddd;height:32px;padding-left:14px;position:relative}
.links li::before{content:"";position:absolute;left:0;top:7px;width:4px;height:4px;background:#ddd;border-radius:50%}
.contact{position:absolute;left:317px;font-size:12px;color:#ddd;line-height:18px;padding-left:30px}
.contact svg{position:absolute;left:0;top:1px}
.feed{position:absolute;left:655px;width:290px;height:52px;padding-left:56px}
.feed .sq{position:absolute;left:0;top:0;width:44px;height:44px;border:1px solid #555;background:#2d2d2d}
.feed .sq i{position:absolute;left:14px;top:14px;width:14px;height:14px;border-radius:50%;background:#5a6f9a}
.feed b{font-size:10px;color:#6f8fd0;font-weight:600}
.feed span{font-size:10px;color:#999;margin-left:10px}
.feed p{font-size:10.5px;color:#ccc;margin-top:4px}
.glass-art{position:absolute;left:1020px;top:40px;width:124px;height:248px;background:linear-gradient(180deg,#2c2c2c,#232323)}

/* copyright */
.copyright{top:4514px;height:55px;background:var(--wine-deep)}
.copyright .txt{position:absolute;left:82px;top:20px;font-size:11px;color:#fff;font-weight:600}
.copyright .follow{position:absolute;left:946px;top:19px;font-size:12px;color:#fff;font-weight:700}
.social{position:absolute;top:13px;width:28px;height:28px;border-radius:50%;background:#3b5f9e}
</style>
</head>
<body>

<!-- top bar -->
<section class="topbar">
  <div class="item phone">
    <svg width="14" height="14" viewBox="0 0 24 24"><path fill="#fff" d="M6.6 10.8a15 15 0 0 0 6.6 6.6l2.2-2.2c.3-.3.7-.4 1-.2 1.1.4 2.3.6 3.6.6.6 0 1 .4 1 1V20c0 .6-.4 1-1 1A17 17 0 0 1 3 4c0-.6.4-1 1-1h3.5c.6 0 1 .4 1 1 0 1.3.2 2.5.6 3.6.1.3 0 .7-.2 1z"/></svg>555 0142
  </div>
  <div class="item" style="left:720px">
    <svg width="14" height="14" viewBox="0 0 24 24"><rect x="3" y="8" width="18" height="13" fill="none" stroke="#fff" stroke-width="2"/><path d="M12 8v13M3 12h18" stroke="#fff" stroke-width="2"/></svg>BUY GIFT CERTIFICATES
  </div>
  <div class="item" style="left:940px">
    <svg width="14" height="14" viewBox="0 0 24 24"><path d="M6 3v8M4 3v5a2 2 0 0 0 4 0V3M6 11v10M17 3c-2 0-3 3-3 7h3v11" stroke="#fff" stroke-width="2" fill="none"/></svg>ONLINE RESERVATION
  </div>
</section>

<!-- header -->
<header class="site-header">
  <div class="abs brand"><span class="brand-dot"></span>VELLORA BISTRO</div>
  <nav class="abs nav">
    <a href="#">Home</a><a href="#">About Us</a><a href="#">Menu</a><a href="#">Gallery</a><a href="#">Blog</a><a href="#">Contact Us</a>
  </nav>
</header>

<!-- hero -->
<section class="hero">
  <div class="hero-photo" role="img" aria-label="Glass of red wine on a rustic wooden table beside a wine bottle and burlap"></div>
  <h1>Vellora Bistro<br>italian restaurant<br>in Cabo San Lucas</h1>
  <div class="dots"><i></i><i></i><i></i><i></i></div>
  <div class="scallop-bottom"></div>
</section>

<!-- welcome -->
<section class="welcome">
  <div class="abs center title" style="top:47px">Welcome to <em>Vellora Bistro</em> Italian Cuisine &amp; Wine Bar</div>
  <div class="rule" style="top:99px"></div>
  <div class="abs center lead" style="top:112px">Lorem ipsum dolor sit amet, consectetuer adipiscing elit, sed diam nonummy nibh euismod tincidunt ut laoreet dolore magna aliquam erat</div>
  <p class="abs body" style="left:120px;top:142px;width:960px;text-align:center">Lorem ipsum dolor sit amet, consectetuer adipiscing elit, sed diam nonummy nibh euismod tincidunt ut laoreet dolore magna aliquam erat volutpat. Ut wisi enim ad minim veniam, quis nostrud exerci tation ullamcorper suscipit lobortis nisl ut aliquip ex ea commodo consequat. Duis autem vel eum iriure dolor in hendrerit in vulputate velit esse molestie consequat, vel illum dolore eu feugiat nulla facilisis at vero eros et accumsan et iusto odio dignissim qui blandit praesent luptatum zzril delenit augue duis dolore. Lorem ipsum dolor sit amet, consectetuer adipiscing elit, sed diam nonummy nibh euismod tincidunt ut laoreet dolore magna aliquam erat volutpat.</p>
  <div class="abs center" style="top:286px"><span class="btn" style="background:var(--wine)">Read More</span></div>
  <div class="scallop-bottom" style="--edge:#17110e;transform:scaleY(-1);bottom:-1px"></div>
</section>

<!-- reservation -->
<section class="reserve" role="img" aria-label="Dark restaurant table setting with wine glasses, behind the reservation form">
  <div class="abs center title light" style="top:64px">Book Online Reservation</div>
  <div class="rule light" style="top:113px"></div>
  <div class="abs center lead light-text" style="top:131px;color:#fff">Lorem ipsum dolor sit amet, consectetuer adipiscing elit, sed diam nonummy nibh euismod tincidunt ut laoreet dolore magna aliquam erat</div>
  <div class="field" style="left:82px">Name *</div>
  <div class="field" style="left:292px">Phone *</div>
  <div class="field" style="left:503px">no of guest</div>
  <div class="field" style="left:713px">Message</div>
  <div class="submit">SUBMIT</div>
  <div class="scallop-bottom" style="--edge:#fafafa"></div>
</section>

<!-- menu -->
<section class="menu">
  <div class="abs center title" style="top:40px">Our <em>Menu Items</em></div>
  <div class="rule" style="top:90px"></div>
  <p class="abs body" style="left:140px;top:100px;width:920px;text-align:center">Lorem ipsum dolor sit amet, consectetuer adipiscing elit, sed diam nonummy nibh euismod tincidunt ut laoreet dolore magna aliquam erat volutpat. Ut wisi enim ad minim veniam, quis nostrud exerci tation ullamcorper suscipit lobortis nisl ut aliquip ex ea commodo consequat.</p>
  <div class="dish" style="left:82px;top:179px;background:linear-gradient(135deg,#f4efe6,#c9b48f 55%,#5a3b1c)" role="img" aria-label="Row of premium beer bottles"><div class="label">Premium Beer</div></div>
  <div class="dish" style="left:436px;top:179px;background:linear-gradient(135deg,#2a1b10,#8a5a2b 50%,#3a2414)" role="img" aria-label="Wooden beer barrel with glasses of beer"><div class="label">Beer</div></div>
  <div class="dish" style="left:789px;top:179px;background:linear-gradient(135deg,#3a2210,#b8742c 50%,#4a2a14)" role="img" aria-label="Warmly lit bar interior at night"><div class="label">Nightcap</div></div>
  <div class="dish" style="left:82px;top:423px;background:linear-gradient(135deg,#e8e2da,#9a7c60 55%,#4a3020)" role="img" aria-label="Cup of coffee on coffee beans"><div class="label">Coffees</div></div>
  <div class="dish" style="left:436px;top:423px;background:linear-gradient(135deg,#5a3420,#a0683f 50%,#3a1f12)" role="img" aria-label="Chocolate cake slices"><div class="label">Desserts</div></div>
  <div class="dish" style="left:789px;top:423px;background:linear-gradient(135deg,#f1d64a,#e9c889 50%,#c9b06a)" role="img" aria-label="Bowl of pasta soup"><div class="label">Sopas</div></div>
</section>

<!-- atmosphere -->
<section class="atmos">
  <div class="scallop-top" style="--edge:#fafafa"></div>
  <div class="abs center title light" style="top:66px">Unforgettable Atmosphere</div>
  <div class="rule light" style="top:114px"></div>
  <div class="abs center lead" style="top:134px;color:#fff">A GOOD INTERIOR DESIGN CAN DO AS MUCH FOR A CAFE, RESTARANT OR BAR AS GOOD FOOD AND DRINKS CAN.</div>
  <p class="abs body" style="left:110px;top:164px;width:980px;text-align:center;color:#fff">Lorem ipsum dolor sit amet, consectetuer adipiscing elit, sed diam nonummy nibh euismod tincidunt ut laoreet dolore magna aliquam erat volutpat. Ut wisi enim ad minim veniam, quis nostrud exerci tation ullamcorper Lorem ipsum dolor sit amet, consectetuer adipiscing elit, sed diam nonummy nibh euismod tincidunt</p>
  <div class="abs center" style="top:239px"><span class="btn outline">Online Reservations</span></div>
  <div class="scallop-bottom" style="--edge:#f3f3f3"></div>
</section>

<!-- blog -->
<section class="blog">
  <div class="abs center title" style="top:56px">Latest <em>Blog Posts</em></div>
  <div class="rule" style="top:106px"></div>
  <p class="abs" style="left:100px;top:122px;width:1000px;text-align:center;font-size:12px;line-height:20px;font-weight:700;color:var(--ink)">Lorem ipsum dolor sit amet, consectetuer adipiscing elit, sed diam nonummy nibh euismod tincidunt ut laoreet dolore magna aliquam erat volutpat. Ut wisi enim ad minim veniam, quis nostrud exerci tation ullamcorper suscipit lobortis nisl ut aliquip ex ea commodo consequat. Duis autem vel eum iriure dolor</p>
  <article class="post" style="left:82px">
    <div class="pic" style="background:linear-gradient(135deg,#3a72c4,#d9c8a0 50%,#8a6a3a)" role="img" aria-label="Bowl of stew with vegetables"><div class="date"><b>24</b><span>JULY</span><span style="margin-top:8px">2017</span></div></div>
    <h3>Lorem Ipsum Dolor</h3>
    <p>Sed ut perspiciatis unde omnis iste natus error sit voluptatem accusa nt ium doloremque laudantium totam rem aperiam eaque ipsa</p>
    <div class="meta"><b>By</b> | Sed ut perspiciatis &nbsp;&nbsp;&nbsp; <b>0</b> Comments</div>
  </article>
  <article class="post" style="left:436px">
    <div class="pic" style="background:linear-gradient(135deg,#d8b070,#9a5a2a 50%,#e2c28a)" role="img" aria-label="Burger with fries and sides on a table"><div class="date"><b>24</b><span>JULY</span><span style="margin-top:8px">2017</span></div></div>
    <h3>Lorem Ipsum Dolor</h3>
    <p>Sed ut perspiciatis unde omnis iste natus error sit voluptatem accusa nt ium doloremque laudantium totam rem aperiam eaque ipsa</p>
    <div class="meta"><b>By</b> | Sed ut perspiciatis &nbsp;&nbsp;&nbsp; <b>0</b> Comments</div>
  </article>
  <article class="post" style="left:789px">
    <div class="pic" style="background:linear-gradient(135deg,#f0ece4,#c88a3a 50%,#6a3a1a)" role="img" aria-label="Cheeseburger close-up"><div class="date"><b>24</b><span>JULY</span><span style="margin-top:8px">2017</span></div></div>
    <h3>Lorem Ipsum Dolor</h3>
    <p>Sed ut perspiciatis unde omnis iste natus error sit voluptatem accusa nt ium doloremque laudantium totam rem aperiam eaque ipsa</p>
    <div class="meta"><b>By</b> | Sed ut perspiciatis &nbsp;&nbsp;&nbsp; <b>0</b> Comments</div>
  </article>
</section>

<!-- customers -->
<section class="customers" role="img" aria-label="Blurred diners enjoying a meal, behind the testimonials">
  <div class="abs center title light" style="top:60px">Our Happy Customers</div>
  <div class="rule light" style="top:110px"></div>
  <svg class="arrow" style="left:158px" width="20" height="40" viewBox="0 0 20 40"><path d="M16 4 4 20l12 16" stroke="#fff" stroke-width="2" fill="none"/></svg>
  <svg class="arrow" style="left:1022px" width="20" height="40" viewBox="0 0 20 40"><path d="M4 4l12 16L4 36" stroke="#fff" stroke-width="2" fill="none"/></svg>
  <div class="avatar" style="left:225px" role="img" aria-label="Customer portrait"></div>
  <div class="avatar" style="left:448px" role="img" aria-label="Customer portrait"></div>
  <div class="avatar" style="left:667px" role="img" aria-label="Customer portrait"></div>
  <div class="avatar" style="left:868px" role="img" aria-label="Customer portrait"></div>
  <div class="cname" style="left:177px">Miss Lara Vento</div>
  <div class="cname" style="left:400px">Mr. Dario Pellin</div>
  <div class="cname" style="left:619px">Miss Lara Vento</div>
  <div class="cname" style="left:820px">Mrs. Nora Pellin</div>
  <div class="quote"><span class="mark">&ldquo;</span>Lorem ipsum dolor sit amet, consectetuer adipiscing elit, sed diam nonummy nibh euismod tincidunt ut laoreet dolore magna aliquam erat volutpat. Ut wisi enim ad minim veniam, quis nostrud exerci tation ullamcorper suscipit lobortis nisl ut aliquip ex ea commodo consequat. Duis autem vel eum iriure dolor in hendrerit in vulputate velit esse molestie consequat.</div>
</section>

<!-- wine tours -->
<section class="tours">
  <div class="band">
    <div class="abs center title light" style="top:62px">Wine Tours</div>
    <div class="rule light" style="top:110px"></div>
    <div class="abs center lead" style="top:130px;color:#fff">Lorem ipsum dolor sit amet, consectetuer adipiscing elit, sed diam nonummy nibh euismod tincidunt ut laoreet dolore magna aliquam erat</div>
  </div>
  <article class="tour" style="left:82px">
    <div class="pic" style="background:linear-gradient(135deg,#6a8a4a,#8a4a2a 45%,#c89a6a)" role="img" aria-label="Wine bottle and glasses on a barrel in a vineyard"></div>
    <h3>Wine Tasting Tours</h3>
    <p>Lorem ipsum dolor sit amet, consectetuer adipiscing elit, sed diam nonummy nibh euismod tincidunt ut laoreet dolore magna aliquam erat volutpat. Ut wisi enim ad minim veniam, quis nostrud exerci tation ullamcorper suscipit</p>
  </article>
  <article class="tour" style="left:615px">
    <div class="pic" style="background:linear-gradient(135deg,#3a2a22,#8a2a2a 40%,#e8dcc4)" role="img" aria-label="Red wine bottle and glass with cheese wheels"></div>
    <h3>Wine Pairing Tours</h3>
    <p>Lorem ipsum dolor sit amet, consectetuer adipiscing elit, sed diam nonummy nibh euismod tincidunt ut laoreet dolore magna aliquam erat volutpat. Ut wisi enim ad minim veniam, quis nostrud exerci tation ullamcorper suscipit</p>
  </article>
  <div class="scallop-bottom" style="--edge:#222"></div>
</section>

<!-- footer -->
<footer class="site-footer">
  <h4 style="left:82px">Quick Links</h4>
  <ul class="links"><li>Home</li><li>About Us</li><li>Menu</li><li>Gallery</li><li>Blog</li><li>Contact Us</li></ul>

  <h4 style="left:317px">Contact Details</h4>
  <div class="contact" style="top:96px">
    <svg width="14" height="18" viewBox="0 0 24 30"><path d="M12 0a10 10 0 0 0-10 10c0 8 10 20 10 20s10-12 10-20A10 10 0 0 0 12 0zm0 14a4 4 0 1 1 0-8 4 4 0 0 1 0 8z" fill="#fff"/></svg>
    <b style="color:#fff">VELLORA BISTRO</b><br>Calle Olmo 12, Centro<br>Cabo San Lucas, Mexico
  </div>
  <div class="contact" style="top:196px">
    <svg width="14" height="14" viewBox="0 0 24 24"><path fill="#fff" d="M6.6 10.8a15 15 0 0 0 6.6 6.6l2.2-2.2c.3-.3.7-.4 1-.2 1.1.4 2.3.6 3.6.6.6 0 1 .4 1 1V20c0 .6-.4 1-1 1A17 17 0 0 1 3 4c0-.6.4-1 1-1h3.5c.6 0 1 .4 1 1 0 1.3.2 2.5.6 3.6.1.3 0 .7-.2 1z"/></svg>555 0142
  </div>
  <div class="contact" style="top:254px">
    <svg width="16" height="12" viewBox="0 0 24 18"><rect x="1" y="1" width="22" height="16" fill="none" stroke="#fff" stroke-width="2"/><path d="M1 1l11 9 11-9" fill="none" stroke="#fff" stroke-width="2"/></svg>info@vellorabistro.com
  </div>

  <h4 style="left:655px">Chatterbay Feeds</h4>
  <div class="feed" style="top:88px"><div class="sq"><i></i></div><b>Elsa Marin</b><span>1:56 PM November 23rd</span><p>November is the month of the harvest menu</p></div>
  <div class="feed" style="top:152px"><div class="sq"><i></i></div><b>Elsa Marin</b><span>1:56 PM November 23rd</span><p>November is the month of the harvest menu</p></div>
  <div class="feed" style="top:216px"><div class="sq"><i></i></div><b>Elsa Marin</b><span>1:56 PM November 23rd</span><p>November is the month of the harvest menu</p></div>

  <div class="glass-art" role="img" aria-label="Line drawing of a wine glass"></div>
</footer>

<!-- copyright -->
<section class="copyright">
  <div class="txt">COPYRIGHT © 2017 VELLORA BISTRO. ALL RIGHTS RESERVED.</div>
  <div class="follow">FOLLOW US:</div>
  <span class="social" style="left:1030px" aria-label="Chatterbay"></span>
  <span class="social" style="left:1062px;background:#3aa6d8" aria-label="Social profile"></span>
  <span class="social" style="left:1094px;background:#c4302b" aria-label="Video channel"></span>
  <span class="social" style="left:1126px;background:#8a3a8a" aria-label="Photo profile"></span>
</section>

</body>
</html>
```